Yoga Shool offering Teacher Training in a new venue

I need to advertise our 200Hr Teacher Training course at the Fernhill Arena, I want to attract yoga students who want to be teachers as well as those looking to deepen their personal practice and attend for personal growth. I introduced yoga classes to this venue when it first opened in 2000, and I am returning with this Teacher Training course. My website colours are brown and orange.

Target Market(s)

Yoga Students around the venue

Font styles to use
Sans Serif

Colors

Designer to choose colors to be used in the design.

Requirements
Must have
• logo,

```html
<!DOCTYPE html>
<html lang="en">
<head>
<meta charset="utf-8">
<title>Tidal Flow Yoga Teacher Training Flyer</title>
<link href="https://fonts.googleapis.com/css2?family=Julius+Sans+One&family=Open+Sans:ital,wght@0,400;0,700;1,700&display=swap" rel="stylesheet">
<style>
  :root {
    --orange: #ee7623;
    --brown: #5f3f43;
    --ink: #3b2b2d;
    --page: #ffffff;
    --backdrop: #ececec;
    --veil: rgba(255, 255, 255, 0.72);
  }
  * { margin: 0; padding: 0; box-sizing: border-box; }
  html, body { width: 1200px; height: 1200px; overflow: hidden; background: var(--backdrop); }
  .flyer {
    position: absolute; left: 205px; top: 42px;
    width: 790px; height: 1117px;
    background: var(--page);
    font-family: "Open Sans", sans-serif;
    color: var(--ink);
  }
  .rule-top, .rule-mid {
    position: absolute; left: 26px; width: 738px; height: 9px; background: var(--orange);
  }
  .rule-top { top: 0; }
  .rule-mid { top: 294px; }
  .brand {
    position: absolute; left: 0; top: 120px; width: 100%;
    display: flex; align-items: center; justify-content: center; gap: 16px;
  }
  .brand-dot { width: 54px; height: 54px; border-radius: 50%; background: var(--brown); }
  .brand-name {
    font-family: "Julius Sans One", sans-serif; font-size: 40px; color: var(--brown);
  }
  .photo {
    position: absolute; left: 26px; top: 303px; width: 738px; height: 735px;
    background: linear-gradient(180deg, #e6ebdf 0%, #eceee6 45%, #e9e4de 75%, #e3ddd8 100%);
  }
  .band {
    position: absolute; left: 0; width: 790px;
    border-top: 2px solid var(--orange); border-bottom: 2px solid var(--orange);
    background: var(--veil);
  }
  .band-venue { top: 414px; height: 51px; }
  .band-step { top: 730px; height: 56px; }
  .line {
    position: absolute; left: 0; width: 100%; text-align: center; white-space: nowrap;
  }
  .headline {
    font-family: "Julius Sans One", sans-serif; color: var(--brown);
    font-size: 52px; line-height: 1;
  }
  .subline {
    font-family: "Julius Sans One", sans-serif; color: var(--brown);
    font-size: 18px; line-height: 1; letter-spacing: 0.5px;
  }
  .strong { font-weight: 700; font-size: 18px; line-height: 1; }
  .strong-small { font-weight: 700; font-size: 15px; line-height: 1; }
  .body { font-size: 15.5px; line-height: 1; }
  .author { font-weight: 700; font-style: italic; font-size: 15.5px; line-height: 1; }
  .cta {
    position: absolute; left: 26px; top: 1038px; width: 738px; height: 79px;
    background: var(--orange); color: #fff; text-align: center;
    font-weight: 700; font-size: 20px; line-height: 24px; padding-top: 15px;
  }
</style>
</head>
<body>
<main class="flyer">
  <div class="rule-top"></div>
  <div class="brand">
    <span class="brand-dot"></span>
    <span class="brand-name">Tidal Flow Yoga</span>
  </div>
  <div class="rule-mid"></div>

  <div class="photo" role="img" aria-label="Faded photo of a smiling woman seated cross-legged on a timber deck in a leafy garden"></div>

  <div class="line headline" style="top:318px">ARE YOU READY?</div>
  <div class="line subline" style="top:378px">TO SET IN MOTION A STUNNING TRANSFORMATION IN 2019</div>

  <div class="band band-venue"></div>
  <div class="line strong" style="top:429px">TIDAL FLOW YOGA TEACHER TRAINING is coming to FERNHILL ARENA</div>

  <div class="line headline" style="top:482px">Do You Love Yoga?</div>
  <div class="line subline" style="top:543px">Do you want to know yourself, love yourself, heal yourself and</div>
  <div class="line subline" style="top:566px">treat yourself better?</div>
  <div class="line headline" style="top:597px">THIS IS FOR YOU!</div>

  <div class="line body" style="top:657px">Tidal Flow Yoga Teacher Training isn’t just for aspiring teachers, it’s for any dedicated</div>
  <div class="line body" style="top:676px">student of yoga to build a powerful personal practice and deepen their understanding</div>
  <div class="line body" style="top:695px">and experience of yoga.</div>

  <div class="band band-step"></div>
  <div class="line strong-small" style="top:741px">TAKE THE NEXT STEP IN YOUR YOGA AND IN YOUR LIFE, ACCESS NEW POSSIBILITIES,</div>
  <div class="line strong-small" style="top:760px">CHECK OUT WHAT PAST TRAINEES HAD TO SAY:</div>

  <div class="line body" style="top:805px"><b>TA</b>“Wow! This course has been life changing in every way,</div>
  <div class="line body" style="top:824px">it has given me so much confidence to do things I haven’t done before.”</div>
  <div class="line author" style="top:844px">Jo Marden 2018</div>

  <div class="line body" style="top:874px">“I love how we apply everything to our own lives – it’s real and tangible,</div>
  <div class="line body" style="top:893px">so we live it and learn it...”</div>
  <div class="line author" style="top:912px">Lena Hart Quill 2016</div>

  <div class="line body" style="top:942px">“I loved every lesson, and as I applied the teachings to my life,</div>
  <div class="line body" style="top:961px">they had a flow on effect to my family too. Prepare to not only become a yoga teacher,</div>
  <div class="line body" style="top:980px">prepare to change in incredibly positive ways.”</div>
  <div class="line author" style="top:999px">Mira Dalton 2018</div>

  <div class="cta">Course Details are available on our website<br>www.tidalflowyoga.com.au</div>
</main>
</body>
</html>
```